Korvalin Solutions needs mailable brochure design

We need a brochure design that we can mail via the post office (trifold), plus mail online (html format). We would like the brochure to highlight on the services we are offering. We would like the colors to match those that are in our logo which is attached. I've included some text in addition to jpeg images that you may want to consider using. The transfer fees we refer to in the text is related to geophysical seismic data

Target Market(s)

Energy companies

Industry/Entity Type

Oil And Gas

```html
<!DOCTYPE html>
<html lang="en">
<head>
<meta charset="utf-8">
<title>Korvalin Solutions – Brochure</title>
<link href="https://fonts.googleapis.com/css2?family=Arimo:wght@400;700&family=Roboto:wght@300;400&display=swap" rel="stylesheet">
<style>
  :root {
    --ink: #1f1f1f;
    --panel-dark: #202024;
    --sky: #cfe8f6;
    --blue: #1ea0e6;
    --navy: #2c3566;
    --orange: #f07830;
    --grey-text: #5a5a5a;
    --icon-bg: #bfe3f3;
    --white: #ffffff;
  }
  * { box-sizing: border-box; margin: 0; padding: 0; }
  html, body { width: 1200px; height: 927px; overflow: hidden; background: var(--white); }
  body { font-family: "Arimo", Arial, sans-serif; color: var(--ink); position: relative; }

  .top-strip { position: absolute; left: 403px; top: 0; width: 797px; height: 42px; background: var(--sky); }

  .brand-block { position: absolute; left: 0; top: 42px; width: 403px; height: 268px; background: var(--panel-dark); }
  .brand-name { position: absolute; left: 44px; top: 208px; color: var(--white); font-family: "Arimo", Arial, sans-serif; font-weight: 400; font-size: 30px; line-height: 1; }

  .hero-photo { position: absolute; left: 403px; top: 42px; width: 797px; height: 268px;
    background: linear-gradient(135deg, #eef7fc 0%, #d6ecf8 40%, #9fd0ee 70%, #3a6f9a 100%); }

  .side-panel { position: absolute; left: 0; top: 310px; width: 403px; height: 574px;
    background: linear-gradient(90deg, #e6e8ea 0%, #f7f8f9 45%, #f2f3f4 75%, #dfe1e3 100%); }
  .side-panel .statement { position: absolute; left: 43px; font-family: "Roboto", Arial, sans-serif; font-weight: 300; color: var(--grey-text); font-size: 36px; line-height: 37px; letter-spacing: -0.6px; }
  .statement-data { top: 68px; }
  .statement-years { top: 212px; }
  .statement-advisor { top: 392px; }
  .accent-blue { color: var(--blue); font-weight: 400; }
  .accent-navy { color: var(--navy); font-weight: 400; }
  .accent-orange { color: var(--orange); font-weight: 400; }
  .side-rule { position: absolute; left: 43px; width: 324px; height: 2px; background: var(--navy); }
  .rule-1 { top: 193px; }
  .rule-2 { top: 375px; }

  .corner-tab { position: absolute; left: 403px; top: 311px; }

  .body-copy { font-size: 13.2px; line-height: 16.7px; color: var(--ink); }
  .body-copy p { margin-bottom: 8.3px; }
  .col-main { position: absolute; left: 441px; top: 339px; width: 334px; }
  .archive-photo { position: absolute; left: 834px; top: 342px; width: 172px; height: 202px;
    background: linear-gradient(180deg, #e9e6dd 0%, #b9b6ac 45%, #3f4246 70%, #cfcac0 100%); }
  .col-side { position: absolute; left: 1024px; top: 339px; width: 122px; }
  .col-lower { position: absolute; left: 834px; top: 557px; width: 330px; }

  .services { position: absolute; left: 403px; top: 742px; width: 797px; }
  .service { position: absolute; width: 220px; text-align: center; }
  .service .icon { display: block; margin: 0 auto; width: 90px; height: 90px; border-radius: 50%; background: var(--icon-bg); }
  .service .label { display: block; margin-top: 13px; font-size: 14.5px; font-weight: 400; color: var(--ink); }
  .svc-1 { left: 39px; }
  .svc-2 { left: 293px; }
  .svc-3 { left: 543px; }

  .footer-band { position: absolute; left: 403px; top: 881px; width: 797px; height: 46px; background: var(--orange);
    color: var(--white); font-size: 14px; letter-spacing: 2.4px; display: flex; align-items: center; justify-content: center; }
  .footer-band strong { font-weight: 700; margin-right: 6px; }
</style>
</head>
<body>
  <div class="top-strip"></div>

  <header class="brand-block">
    <div class="brand-name">Korvalin Solutions</div>
  </header>

  <div class="hero-photo" role="img" aria-label="Close-up of business charts with blue bar graphs, eyeglasses and a newspaper on a desk"></div>

  <aside class="side-panel" role="img" aria-label="Soft-focus data server room aisle">
    <p class="statement statement-data">Transforming Data<br>into <span class="accent-blue">Reliable<br>Information</span></p>
    <div class="side-rule rule-1"></div>
    <p class="statement statement-years">We bring over<br><span class="accent-navy">50 years of<br>experience</span> in Oil &amp;<br>Gas Industry</p>
    <div class="side-rule rule-2"></div>
    <p class="statement statement-advisor"><span class="accent-orange">We are the trusted<br>advisor</span> to the<br>world's leading<br>businesses</p>
  </aside>

  <svg class="corner-tab" width="30" height="56" viewBox="0 0 30 56">
    <path d="M2.5 56 V2.5 H30" fill="none" stroke="#f07830" stroke-width="5"/>
  </svg>

  <section class="body-copy col-main">
    <p>It goes without saying that if you are an E&amp;P company, large or small, you are data rich. Data, whether it be well, seismic, geological, reports, or studies are the foundation on which many decisions are made. As companies continue to gather and acquire these rather extensive data sets, they must not only continue to ask themselves a series of questions to assure they are in a position to locate and use this valuable asset, but what is the impact of potential Transfer Fees.</p>
    <p>Transfer Fees are triggered due to a third-party merger, or acquisition of the data license holder.</p>
    <p>Companies may overlook these fees as a result of limited access to records, loss of records during a merger or acquisition, scarce internal resources, or insufficient knowledge and experience.</p>
    <p>The financial impact of these fees could reach into the millions of dollars based on the size of your licensed data inventories.</p>
    <p>Korvalin Solutions can help mitigate your exposure.</p>
  </section>

  <div class="archive-photo" role="img" aria-label="Archive room with rows of dark storage shelving"></div>

  <section class="body-copy col-side">
    <p>We have over fifty years of upstream seismic asset experience within a Fortune 100 company.</p>
    <p>We have a wide range of Transfer Fee experiences both with active and non-active mergers/ acquisitions.</p>
  </section>

  <section class="body-copy col-lower">
    <p>The ability to know whether or not your data is licensed or proprietary is critical.&nbsp; Data ownership determines not only how the data and the derivatives created from those data sets are handled internally and externally, but to a very large extent the potential financial and operational impact should you become part of a merger or acquisition. Likewise, these same issues present themselves to companies to whom you've licensed data during a merger or acquisition.</p>
  </section>

  <section class="services">
    <div class="service svc-1"><span class="icon" role="img" aria-label="Illustration of a hand pointing at a light bulb"></span><span class="label">DATA MANAGEMENT</span></div>
    <div class="service svc-2"><span class="icon" role="img" aria-label="Illustration of a keyboard, screen and pen"></span><span class="label">BUSINESS CONSULTING</span></div>
    <div class="service svc-3"><span class="icon" role="img" aria-label="Illustration of interlocking gears"></span><span class="label">DATA SERVICES</span></div>
  </section>

  <footer class="footer-band"><strong>KORVALIN</strong> can provide the aide to mitigate financial and operational exposure.</footer>
</body>
</html>
```